Business card, Letterhead and envelope design
Create a business card, letterhead and envelope design for Velmira Solutions
Professional
name
title
address
email@velmira-example.com
www.velmirasolutions-example.com
logo and font
Trifold brochure design we have for inspiration of design. This is for reference only.

```html
<!DOCTYPE html>
<html lang="en">
<head>
<meta charset="utf-8">
<title>Velmira Solutions Stationery</title>
<link rel="stylesheet" href="https://fonts.googleapis.com/css2?family=Exo+2:wght@400;700&display=swap">
<style>
  :root {
    --backdrop: #1c1c1c;
    --paper: #ffffff;
    --paper-shade: #e9ecef;
    --blue-deep: #0a3fc4;
    --blue-mid: #1f74f0;
    --blue-light: #8cc6ff;
    --ink: #1a1a1a;
    --ink-soft: #555a60;
  }
  * { box-sizing: border-box; margin: 0; padding: 0; }
  html, body { width: 1200px; height: 765px; overflow: hidden; }
  body { background: var(--backdrop); font-family: "Exo 2", sans-serif; color: var(--ink); }
  .stage { position: relative; width: 1200px; height: 765px; }

  .sheet { position: absolute; overflow: hidden; background: linear-gradient(180deg, var(--paper) 60%, var(--paper-shade)); }
  .sheet .swoosh { position: absolute; left: 0; top: 0; }

  .brand { position: absolute; display: flex; flex-direction: column; }
  .brand-mark { background: var(--ink); }
  .brand-name { font-weight: 700; color: var(--ink); line-height: 0.95; }

  /* Letterhead */
  .letterhead { left: 497px; top: 24px; width: 480px; height: 710px; }
  .letterhead .brand { left: 28px; top: 40px; }
  .letterhead .brand-mark { width: 52px; height: 52px; margin-bottom: 10px; margin-left: 4px; }
  .letterhead .brand-name { font-size: 22px; }
  .letterhead-footer { position: absolute; left: 0; right: 0; bottom: 22px; text-align: center; font-size: 7.5px; line-height: 1.55; color: var(--ink-soft); }

  /* Envelope */
  .envelope { left: 29px; top: 293px; width: 667px; height: 384px; box-shadow: 6px 8px 18px rgba(0,0,0,0.45); }
  .envelope .brand { left: 38px; top: 104px; }
  .envelope .brand-mark { width: 66px; height: 66px; margin-bottom: 10px; margin-left: 6px; }
  .envelope .brand-name { font-size: 28px; }
  .envelope-address { position: absolute; left: 38px; top: 250px; font-size: 8px; color: var(--ink-soft); }

  /* Business card */
  .card { left: 941px; top: 163px; width: 228px; height: 142px; box-shadow: 4px 6px 12px rgba(0,0,0,0.4); }
  .card .brand { left: 12px; top: 48px; }
  .card .brand-mark { width: 34px; height: 34px; margin-bottom: 6px; margin-left: 2px; }
  .card .brand-name { font-size: 15px; }
  .card-contact { position: absolute; right: 12px; top: 32px; text-align: right; font-size: 5.5px; line-height: 1.5; color: var(--ink-soft); }
  .card-contact .holder { font-size: 8px; font-weight: 700; color: var(--blue-deep); }
</style>
</head>
<body>
<main class="stage">

  <section class="sheet letterhead" aria-label="Letterhead">
    <svg class="swoosh" width="480" height="120" viewBox="0 0 480 120">
      <defs>
        <linearGradient id="lh-blue" x1="0" y1="0" x2="1" y2="1">
          <stop offset="0" stop-color="var(--blue-deep)"/>
          <stop offset="0.55" stop-color="var(--blue-mid)"/>
          <stop offset="1" stop-color="var(--blue-deep)"/>
        </linearGradient>
      </defs>
      <path d="M0 0 H480 V55 C380 30 250 40 150 65 C90 80 40 80 0 72 Z" fill="url(#lh-blue)"/>
      <path d="M0 78 C45 86 95 85 155 70 C255 46 385 36 480 60 V66 C385 42 255 52 160 76 C95 92 45 92 0 84 Z" fill="var(--blue-light)" opacity="0.8"/>
      <path d="M180 0 C260 40 360 45 480 25 V0 Z" fill="#ffffff" opacity="0.12"/>
    </svg>
    <div class="brand">
      <span class="brand-mark"></span>
      <span class="brand-name">Velmira<br>Solutions</span>
    </div>
    <footer class="letterhead-footer">
      <p>48 Birch Hollow Ct., Lake Harlow, IL 60000</p>
      <p>Toll Free 800-555-0142 | Office 773-555-0187 | Fax 847-555-0163</p>
      <p>Email email@velmira-example.com | www.velmirasolutions-example.com</p>
    </footer>
  </section>

  <section class="sheet envelope" aria-label="Envelope">
    <svg class="swoosh" width="667" height="200" viewBox="0 0 667 200">
      <defs>
        <linearGradient id="env-blue" x1="0" y1="0" x2="1" y2="1">
          <stop offset="0" stop-color="var(--blue-mid)"/>
          <stop offset="0.5" stop-color="var(--blue-deep)"/>
          <stop offset="1" stop-color="var(--blue-mid)"/>
        </linearGradient>
      </defs>
      <path d="M0 0 H667 V130 C560 88 420 96 300 128 C200 154 90 154 0 138 Z" fill="url(#env-blue)"/>
      <path d="M0 144 C90 160 200 160 300 134 C420 102 560 96 667 136 V144 C560 106 420 112 305 142 C200 168 90 168 0 152 Z" fill="var(--blue-light)" opacity="0.8"/>
      <path d="M250 0 C340 60 480 70 667 30 V0 Z" fill="#ffffff" opacity="0.12"/>
    </svg>
    <div class="brand">
      <span class="brand-mark"></span>
      <span class="brand-name">Velmira<br>Solutions</span>
    </div>
    <p class="envelope-address">48 Birch Hollow Ct., Lake Harlow, IL 60000</p>
  </section>

  <section class="sheet card" aria-label="Business card">
    <svg class="swoosh" width="228" height="142" viewBox="0 0 228 142">
      <defs>
        <linearGradient id="card-blue" x1="1" y1="0" x2="0" y2="1">
          <stop offset="0" stop-color="var(--blue-deep)"/>
          <stop offset="1" stop-color="var(--blue-mid)"/>
        </linearGradient>
      </defs>
      <path d="M0 0 H228 V18 C160 10 80 14 0 26 Z" fill="url(#card-blue)"/>
      <path d="M0 30 C80 18 160 14 228 22 V25 C160 18 80 22 0 34 Z" fill="var(--blue-light)" opacity="0.8"/>
    </svg>
    <div class="card-contact">
      <p class="holder">Alex Moran</p>
      <p>Project Manager</p>
      <p>48 Birch Hollow Ct.</p>
      <p>Lake Harlow, IL 60000</p>
      <p>Toll Free 800-555-0142</p>
      <p>Office 773-555-0187</p>
      <p>Fax 847-555-0163</p>
      <p>email@velmira-example.com</p>
      <p>www.velmirasolutions-example.com</p>
    </div>
    <div class="brand">
      <span class="brand-mark"></span>
      <span class="brand-name">Velmira<br>Solutions</span>
    </div>
  </section>

</main>
</body>
</html>
```